website for local kavenda practicioner and yoga teacher trainer

The website should function primarily as:
A place where people can discover Kavenda and book sessions.
A central hub connecting all of my work.
A professional home that reflects my personality and approach.
Website design for Liesbet Oonwerk — Kavenda® Structural Integration practitioner, movement educator, yoga teacher and teacher trainer.
A website that can grow with future projects.
The website should feel: Warm, Human, Invitational, Professional, Accessible, Intelligent, Calm, Clear, Playful, Exploratory, Trustworthy
Avoid: New age aesthetics, Mystical clichés, Excessive spirituality, ”Guru" vibes, Overly clinical design, Corporate wellness branding, Busy layouts
Think: modern, grounded, curious and real.
My work combines three interconnected areas:
1.Bodywork: Touch, structure, awareness and one-on-one support.
2. Movement: Yoga, Pilates and embodied movement.
3. Education: Teacher trainings, workshops and continued learning.
Underlying values:
Curiosity over certainty
Possibility over perfection
Complexity without overwhelm
Science and lived experience together
Exploration rather than dogma
Human beings before methods
The primary goal of the website is to introduce people to Kavenda® Structural Integration and make it easy for them to:
Understand what Kavenda is
Discover whether it might be relevant for them
Learn what to expect from a session
Book an appointment
Booking should always feel visible and easy.
Secondary Goal: Present all other aspects of my work in one coherent place:
Yoga classes
Pilates classes
Teacher trainings
Workshops
Retreats
One-on-one movement sessions
Collaborations with studios
Website Structure
1: HOME
1.1.Hero Section: Large welcoming image
1.2 Two Main Pathways
- Bodywork: Kavenda® Structural Integration
- Movement & Education: Yoga, Pilates, trainings, workshops and retreats
- About Preview: Small introduction with portrait. + Button:
Read More
1.3 Current Events / What's Coming Up: Upcoming trainings, workshops and retreats. (This section should be easy to update)
1.4. Contact / Newsletter: Simple contact information
2: Kavenda® Structural Integration
What is Kavenda?
For whom is it?
What does a session look like?
FAQ
Prices
Booking
Future possibility:
Kaven Movement sessions
3: Movement
- Introductory text.
- Studio Classes (link to “my home base” - > local yoga studio)
- One-to-One Sessions: booking option (this is small; not a key aspect I want to promote)
- Workshops/ Retreats / Teacher Trainings => This section should be flexible and easy to update. Visitors should be able to click into specific offerings.
4. Events
Dynamic page for: Teacher trainings, Retreats, Workshops (see section in movement; here more elaborate)
Each event should contain: Image, Short description, Location, Date, Button for more information. (Linking to hosting studio/location)
5. Work With Me
For studios, organisations and teacher training schools.
Examples: Guest teaching, Workshops, Anatomy, Sequencing, Teacher development , Continuing education -> Clear call-to-action.
Call to action!!=> Book a Session
Prominent button in the navigation.
Footer:
- About Me: Longer biography (6th page)
Personal story and background.
- Testimonials (7th page): Separate page containing testimonials from:
Kavenda clients
Students
Teacher trainees
- Contact: 8th page
Visual Direction
Natural textures. Lots of white space.Editorial feeling.Professional photography.Simple navigation.
Less "wellness influencer.” More:Thoughtful, Contemporary, Timeless, Grounded, Human
Photography should show:
Teaching
Hands-on work
Natural movement
Real interaction
Simplicity
Avoid stereotypical yoga imagery and overly spiritual aesthetics.
Keywords
Warm. Curious. Human. Professional. Embodied. Intelligent. Accessible. Playful. Grounded. Exploratory. Real.
Inspiration / Core Message
Helping people feel more at home in their bodies through touch, movement and education.
The website should communicate that these are not separate services, but different expressions of the same intention:
Bodywork • Movement • Education.
Colours:
light orange/beige: e3d5c4
light orange/off white: f9f7f3
gray azure: 556b78
orange: d07b5a
grey orange: c09f80
dark grey: 3e3e3e
dark gray cyan 2f4f4f
gray green colour: a7c4a0
Fonts: Montserrat and Poppins + raleway
In added documents a try out idea of a website + logo. I will mainly use the logo with diffrent colours (image next to text).
My audience consists of people who want to feel more at home in their bodies and who appreciate a thoughtful, grounded and human approach to movement, touch and education. (30-65yo)
wellbeing
5+ page
- montserrat, poppins, raleway

```html
<!DOCTYPE html>
<html lang="en">
<head>
<meta charset="utf-8">
<title>Liesbet Oonwerk — Kavenda® Structural Integration</title>
<link href="https://fonts.googleapis.com/css2?family=Raleway:wght@400;500&family=Montserrat:wght@500;600;700&family=Poppins:wght@300;400&family=Lora:ital@1&display=swap" rel="stylesheet">
<style>
:root{
  --offwhite:#f9f7f3;
  --sand:#e3d5c4;
  --sand-soft:#f1e7dc;
  --panel:#f4efe8;
  --orange:#d07b5a;
  --greyorange:#c09f80;
  --azure:#556b78;
  --ink:#3e3e3e;
  --slate:#3d4a53;
  --footer:#44535c;
  --green:#a7c4a0;
  --line:#e4dcd2;
}
*{box-sizing:border-box;margin:0;padding:0}
html,body{width:1200px;height:2290px;overflow:hidden;background:var(--offwhite)}
body{position:relative;font-family:'Poppins',sans-serif;color:var(--ink)}
.abs{position:absolute}
.eyebrow{font-family:'Montserrat',sans-serif;font-weight:600;font-size:10px;letter-spacing:1.4px;color:var(--orange);text-transform:uppercase}
.heading{font-family:'Raleway',sans-serif;font-weight:400;color:var(--slate)}
.body{font-size:12px;line-height:21px;color:#4a4a4a;font-weight:400}
.btn{position:absolute;display:flex;align-items:center;justify-content:center;gap:10px;font-family:'Montserrat',sans-serif;font-weight:600;font-size:11px;letter-spacing:1.3px;text-transform:uppercase;text-decoration:none}
.btn-solid{background:var(--orange);color:#fff;border-radius:2px}
.btn-line{border:1.3px solid var(--orange);color:var(--orange);border-radius:2px}
.photo{position:absolute}

/* nav */
.site-header{position:absolute;left:0;top:0;width:1200px;height:108px;background:var(--offwhite);border-bottom:1px solid var(--line)}
.brand{position:absolute;left:42px;top:30px;display:flex;align-items:center;gap:12px}
.brand-dot{width:34px;height:34px;border-radius:50%;background:var(--orange)}
.brand-name{font-family:'Raleway',sans-serif;font-size:26px;color:var(--slate);font-weight:400;line-height:30px}
.brand-tag{font-family:'Montserrat',sans-serif;font-size:6.5px;letter-spacing:.8px;color:var(--slate);font-weight:600;margin-top:2px}
.main-nav{position:absolute;left:345px;top:45px;display:flex;gap:0}
.main-nav a{font-family:'Montserrat',sans-serif;font-size:11px;font-weight:500;letter-spacing:1.1px;color:var(--slate);text-decoration:none;position:absolute;white-space:nowrap}
.main-nav a.active{color:var(--orange)}
.main-nav a.active::after{content:"";position:absolute;left:0;right:0;top:22px;height:1.5px;background:var(--orange)}

/* hero */
.hero{position:absolute;left:0;top:108px;width:1200px;height:516px;overflow:hidden;background:var(--offwhite)}
.hero-photo{left:380px;top:0;width:820px;height:516px;background:linear-gradient(90deg,var(--offwhite) 0%,#f1ebe3 18%,#e6d8c8 42%,#c9a98c 65%,#a8826a 85%,#c9b7a4 100%)}
.hero h1{position:absolute;left:106px;top:110px;font-size:58px;line-height:65px}

/* features */
.feature{position:absolute;top:846px;width:200px}
.feature svg{display:block;margin-bottom:14px}
.feature h3{font-family:'Raleway',sans-serif;font-weight:500;font-size:16px;color:var(--ink);margin-bottom:10px}
.feature p{font-size:11px;line-height:21px;color:#4a4a4a}
.vline{position:absolute;width:1px;background:var(--line)}

/* checklist */
.checklist{position:absolute;left:416px;top:1164px;list-style:none}
.checklist li{display:flex;align-items:center;gap:12px;height:34.7px;font-size:12px;color:var(--ink)}
.tick{width:17px;height:17px;border-radius:50%;background:var(--green);opacity:.8;display:flex;align-items:center;justify-content:center}

/* steps */
.step{position:absolute;top:1436px;width:170px;text-align:center}
.step-num{width:20px;height:20px;border-radius:50%;background:var(--orange);color:#fff;font-family:'Montserrat',sans-serif;font-size:10px;font-weight:600;display:flex;align-items:center;justify-content:center;margin:0 auto}
.step svg{display:block;margin:16px auto 0}
.step h3{font-family:'Raleway',sans-serif;font-weight:500;font-size:16px;color:var(--ink);margin-top:12px}
.step p{font-size:11px;line-height:21px;color:#4a4a4a;margin-top:10px}

/* footer */
.site-footer{position:absolute;left:0;top:2090px;width:1200px;height:200px;background:var(--footer);color:#eef0f0}
.f-col{position:absolute;top:29px}
.f-col h4{font-family:'Montserrat',sans-serif;font-size:9.5px;letter-spacing:1.2px;font-weight:600;margin-bottom:10px}
.f-col a{display:block;font-size:11px;line-height:22.5px;color:#e6eaec;text-decoration:none}
.social{position:absolute;top:2183px;width:42px;height:42px;border-radius:50%;border:1.3px solid #d9dfe2;display:flex;align-items:center;justify-content:center}
</style>
</head>
<body>

<header class="site-header">
  <div class="brand">
    <div class="brand-dot"></div>
    <div>
      <div class="brand-name">Liesbet Oonwerk</div>
      <div class="brand-tag">BODYWORK · MOVEMENT · EDUCATION</div>
    </div>
  </div>
  <nav class="main-nav">
    <a href="#" style="left:0">HOME</a>
    <a href="#" class="active" style="left:79px">KAVENDA®</a>
    <a href="#" style="left:186px">MOVEMENT</a>
    <a href="#" style="left:298px">EVENTS</a>
    <a href="#" style="left:387px">WORK WITH ME</a>
    <a href="#" style="left:524px">ABOUT</a>
    <a href="#" style="left:606px">CONTACT</a>
  </nav>
  <a href="#" class="btn btn-solid" style="left:1041px;top:34px;width:132px;height:37px;font-size:10.5px">BOOK A SESSION</a>
</header>

<section class="hero">
  <div class="photo hero-photo" role="img" aria-label="Practitioner giving a hands-on bodywork session to a client on a treatment table"></div>
  <div class="eyebrow abs" style="left:106px;top:75px">BODYWORK</div>
  <h1 class="heading">Kavenda®<br>Structural<br>Integration</h1>
  <p class="abs" style="left:106px;top:320px;width:350px;font-size:13.5px;line-height:26px;color:var(--ink)">One-on-one bodywork that addresses tension,<br>improves alignment, and enhances the way<br>you move and feel.</p>
  <a href="#" class="btn btn-solid" style="left:106px;top:423px;width:172px;height:40px">BOOK A SESSION <span>→</span></a>
</section>

<section>
  <div class="eyebrow abs" style="left:106px;top:662px;font-size:9px">A BODY IN BALANCE</div>
  <h2 class="heading abs" style="left:106px;top:690px;font-size:32px;line-height:42px">What is<br>Kavenda®?</h2>
  <p class="body abs" style="left:418px;top:683px;width:510px">Kavenda® Structural Integration is a system of manual therapy that works with the body's connective tissue – its structure – to bring more ease, balance and efficiency.</p>
  <p class="body abs" style="left:418px;top:735px;width:510px">Through a series of sessions, we address patterns of tension and restriction that limit your movement and wellbeing. The result is greater alignment, improved function and a deeper sense of being at home in your body.</p>

  <div class="vline" style="left:353px;top:848px;height:150px"></div>
  <div class="vline" style="left:600px;top:848px;height:150px"></div>
  <div class="vline" style="left:847px;top:848px;height:150px"></div>

  <div class="feature" style="left:165px">
    <svg width="40" height="40" viewBox="0 0 40 40" fill="none" stroke="#7a8a93" stroke-width="1.3"><circle cx="20" cy="6" r="3"/><path d="M20 10c-6 5 6 9 0 15s4 8 2 12"/></svg>
    <h3>Structure</h3><p>We work with fascia<br>and connective tissue,<br>not just muscles.</p>
  </div>
  <div class="feature" style="left:411px">
    <svg width="44" height="40" viewBox="0 0 44 40" fill="none" stroke="#7a8a93" stroke-width="1.3"><circle cx="12" cy="8" r="5"/><ellipse cx="12" cy="22" rx="8" ry="5"/><ellipse cx="16" cy="33" rx="13" ry="5"/></svg>
    <h3>Integration</h3><p>Body and mind, support<br>and challenge, science<br>and experience.</p>
  </div>
  <div class="feature" style="left:658px">
    <svg width="46" height="40" viewBox="0 0 46 40" fill="none" stroke="#7a8a93" stroke-width="1.3"><path d="M4 32C4 16 20 6 42 6 40 26 26 34 4 32z"/><path d="M4 32L30 14"/></svg>
    <h3>Balance</h3><p>More ease, mobility and<br>resilience in everyday<br>life and movement.</p>
  </div>
  <div class="feature" style="left:905px">
    <svg width="40" height="40" viewBox="0 0 40 40" fill="none" stroke="#7a8a93" stroke-width="1.3"><circle cx="20" cy="20" r="18"/><circle cx="20" cy="20" r="11"/></svg>
    <h3>You</h3><p>Your body, your story,<br>your pace. This is<br>personal work.</p>
  </div>
  <div class="abs" style="left:373px;top:1042px;width:737px;height:1px;background:var(--line)"></div>
</section>

<section>
  <div class="photo" style="left:0;top:1047px;width:373px;height:312px;background:linear-gradient(135deg,#e9e2d8 0%,#d8c8b6 45%,#b98d74 70%,#8f6a58 100%)" role="img" aria-label="Portrait of the practitioner sitting cross-legged on a wooden floor, smiling"></div>
  <div class="eyebrow abs" style="left:416px;top:1082px;font-size:9px">FOR WHOM?</div>
  <h2 class="heading abs" style="left:416px;top:1108px;font-size:26px">Kavenda® can support you if you…</h2>
  <ul class="checklist">
    <li><span class="tick"><svg width="9" height="9" viewBox="0 0 10 10"><path d="M2 5l2 2 4-4" stroke="#fff" stroke-width="1.5" fill="none"/></svg></span>Feel stiffness, tension or discomfort that keeps coming back</li>
    <li><span class="tick"><svg width="9" height="9" viewBox="0 0 10 10"><path d="M2 5l2 2 4-4" stroke="#fff" stroke-width="1.5" fill="none"/></svg></span>Are recovering from injury or dealing with long-term pain</li>
    <li><span class="tick"><svg width="9" height="9" viewBox="0 0 10 10"><path d="M2 5l2 2 4-4" stroke="#fff" stroke-width="1.5" fill="none"/></svg></span>Want to move with more freedom and less effort</li>
    <li><span class="tick"><svg width="9" height="9" viewBox="0 0 10 10"><path d="M2 5l2 2 4-4" stroke="#fff" stroke-width="1.5" fill="none"/></svg></span>Are curious about your patterns and ready for change</li>
    <li><span class="tick"><svg width="9" height="9" viewBox="0 0 10 10"><path d="M2 5l2 2 4-4" stroke="#fff" stroke-width="1.5" fill="none"/></svg></span>Value a hands-on, attentive and intelligent approach</li>
  </ul>
  <svg class="abs" style="left:860px;top:1062px" width="290" height="335" viewBox="0 0 290 335"><path d="M60 20C120-5 230 10 262 70c30 60 35 140 5 200-30 60-120 80-180 55C30 300 10 240 15 170 20 100 5 45 60 20z" fill="#efe8e1"/></svg>
  <p class="abs" style="left:914px;top:1150px;width:190px;font-family:'Lora',serif;font-style:italic;font-size:16px;line-height:26px;color:var(--slate)"><span style="color:var(--orange)">“</span>After a series of<br>&nbsp;sessions I felt taller,<br>&nbsp;lighter and more<br>&nbsp;at home in my body.<span style="color:var(--orange)">”</span></p>
  <div class="abs" style="left:924px;top:1279px;font-family:'Montserrat',sans-serif;font-size:8.5px;letter-spacing:1.2px;color:#8a8a8a;font-weight:500">– KAVENDA® CLIENT</div>
  <div class="abs" style="left:926px;top:1342px;display:flex;gap:12px">
    <span style="width:6px;height:6px;border-radius:50%;background:var(--orange)"></span>
    <span style="width:6px;height:6px;border-radius:50%;background:#d6cec6"></span>
    <span style="width:6px;height:6px;border-radius:50%;background:#d6cec6"></span>
  </div>
</section>

<section>
  <div class="eyebrow abs" style="left:106px;top:1392px;font-size:9px">THE EXPERIENCE</div>
  <h2 class="heading abs" style="left:106px;top:1418px;font-size:26px;line-height:34px">What does a<br>session look like?</h2>
  <p class="abs" style="left:106px;top:1502px;width:280px;font-size:9.6px;line-height:18px;color:#4a4a4a">Each session is a conversation with your body. Through touch, movement and awareness, we explore how you are organized and where change is possible.</p>
  <p class="abs" style="left:106px;top:1570px;width:280px;font-size:9.6px;line-height:18px;color:#4a4a4a">Sessions take place on a treatment table. You remain fully clothed. The work is deep yet respectful, always adjusted to what is right for you.</p>
  <a href="#" class="btn btn-line" style="left:106px;top:1643px;width:115px;height:33px;font-size:10px">VIEW FAQ <span>→</span></a>

  <div class="vline" style="left:556px;top:1440px;height:220px"></div>
  <div class="vline" style="left:741px;top:1440px;height:220px"></div>
  <div class="vline" style="left:926px;top:1440px;height:220px"></div>

  <div class="step" style="left:380px">
    <div class="step-num">1</div>
    <svg width="48" height="42" viewBox="0 0 48 42" fill="none" stroke="#7a8a93" stroke-width="1.3"><path d="M8 40V16c0-3 4-3 4 0v10M12 14V8c0-3 4-3 4 0v18M40 40V16c0-3-4-3-4 0v10M36 14V8c0-3-4-3-4 0v18"/></svg>
    <h3>Check-in</h3><p>We begin with a short<br>conversation to connect<br>and set an intention.</p>
  </div>
  <div class="step" style="left:564px">
    <div class="step-num">2</div>
    <svg width="48" height="42" viewBox="0 0 48 42" fill="none" stroke="#7a8a93" stroke-width="1.3"><path d="M4 12c7-6 13 6 20 0s13 6 20 0M4 22c7-6 13 6 20 0s13 6 20 0M4 32c7-6 13 6 20 0s13 6 20 0"/></svg>
    <h3>Assessment</h3><p>Through touch and<br>observation I sense<br>how your body is<br>organizing itself.</p>
  </div>
  <div class="step" style="left:749px">
    <div class="step-num">3</div>
    <svg width="52" height="42" viewBox="0 0 52 42" fill="none" stroke="#7a8a93" stroke-width="1.3"><path d="M4 30c4-12 10-18 16-20s4 6 0 10M48 30c-4-12-10-18-16-20s-4 6 0 10M14 36h24"/></svg>
    <h3>Hands-on work</h3><p>Using slow, focused<br>pressure we work<br>with the fascia and<br>underlying structure.</p>
  </div>
  <div class="step" style="left:933px">
    <div class="step-num">4</div>
    <svg width="40" height="42" viewBox="0 0 40 42" fill="none" stroke="#7a8a93" stroke-width="1.3"><circle cx="20" cy="12" r="7"/><path d="M5 40c0-9 7-15 15-15s15 6 15 15z"/></svg>
    <h3>Integration</h3><p>We close with space<br>to feel, move and<br>integrate what<br>has shifted.</p>
  </div>
  <div class="abs" style="left:0;top:1707px;width:1200px;height:1px;background:var(--line)"></div>
</section>

<section class="abs" style="left:0;top:1708px;width:1200px;height:284px;background:var(--panel)">
  <div class="eyebrow abs" style="left:106px;top:38px;font-size:9px">PRICES &amp; BOOKING</div>
  <p class="abs" style="left:106px;top:60px;font-size:12px;color:var(--ink)">Sessions are 60 or 90 minutes.</p>
  <div class="abs" style="left:106px;top:95px;font-family:'Montserrat',sans-serif;font-weight:600;font-size:9px;letter-spacing:1.2px;color:var(--ink)">PRICES</div>
  <div class="abs" style="left:106px;top:112px;font-size:11px;line-height:19px;color:var(--ink)">60 min<br>90 min</div>
  <div class="abs" style="left:180px;top:112px;font-size:11px;line-height:19px;color:var(--ink)">€95<br>€135</div>
  <a href="#" class="btn btn-solid" style="left:106px;top:168px;width:190px;height:35px;font-size:10px">BOOK A SESSION <span>→</span></a>
  <a href="#" class="btn btn-line" style="left:106px;top:216px;width:190px;height:34px;font-size:10px">VIEW PRICES &amp; POLICIES</a>
  <div class="photo" style="left:403px;top:0;width:407px;height:284px;background:linear-gradient(160deg,#efe6da 0%,#e2d2bf 45%,#c9ab8f 75%,#9c7a62 100%)" role="img" aria-label="Calm treatment room with a made-up bodywork table, stool and plants by a bright window"></div>
  <div class="eyebrow abs" style="left:854px;top:38px;font-size:9px">RELATED OFFERING</div>
  <h2 class="heading abs" style="left:854px;top:63px;font-size:20px;line-height:28px">Kaven Movement<br>Sessions</h2>
  <p class="abs" style="left:854px;top:134px;width:190px;font-size:11px;line-height:19.5px;color:#4a4a4a">Movement-based sessions that integrate structure and function through guided movement and embodied exploration.</p>
  <a href="#" class="abs" style="left:854px;top:236px;font-family:'Montserrat',sans-serif;font-weight:600;font-size:10px;letter-spacing:1.3px;color:var(--orange);text-decoration:none">LEARN MORE &nbsp;→</a>
</section>

<section class="abs" style="left:0;top:1992px;width:1200px;height:98px;background:var(--sand-soft)">
  <div class="abs" style="left:99px;top:16px;width:66px;height:66px;border-radius:50%;background:var(--offwhite);display:flex;align-items:center;justify-content:center">
    <svg width="34" height="24" viewBox="0 0 34 24" fill="none" stroke="#6f8a6a" stroke-width="1.6"><rect x="1" y="1" width="32" height="22"/><path d="M1 1l16 12L33 1"/></svg>
  </div>
  <div class="eyebrow abs" style="left:201px;top:23px;font-size:9px">STAY CONNECTED</div>
  <p class="abs" style="left:201px;top:41px;width:200px;font-size:11px;line-height:19px;color:var(--ink)">Get updates on upcoming events, trainings and workshops.</p>
  <div class="abs" style="left:583px;top:34px;width:301px;height:33px;background:#fff;font-size:10.5px;color:#9a9a9a;padding:9px 16px">Your email address</div>
  <a href="#" class="btn btn-solid" style="left:893px;top:34px;width:107px;height:33px;font-size:10px">SUBSCRIBE</a>
</section>

<footer class="site-footer">
  <div class="abs" style="left:59px;top:32px;display:flex;align-items:center;gap:10px">
    <div style="width:30px;height:30px;border-radius:50%;background:var(--orange)"></div>
    <div>
      <div style="font-family:'Raleway',sans-serif;font-size:22px;color:#fff">Liesbet Oonwerk</div>
      <div style="font-family:'Montserrat',sans-serif;font-size:6px;letter-spacing:.8px;color:#e6eaec;font-weight:600">BODYWORK · MOVEMENT · EDUCATION</div>
    </div>
  </div>
  <p class="abs" style="left:59px;top:100px;font-size:11px;line-height:22px;color:#e6eaec">Veldermeer, Lindenland<br>Working locally &amp; internationally</p>
  <div class="f-col" style="left:340px"><h4>BODYWORK</h4><a href="#">Kavenda® Structural Integration</a><a href="#">What is Kavenda®?</a><a href="#">Sessions &amp; Pricing</a><a href="#">Book a Session</a></div>
  <div class="f-col" style="left:546px"><h4>MOVEMENT</h4><a href="#">Studio Classes</a><a href="#">One-to-One Sessions</a><a href="#">Trainings &amp; Education</a><a href="#">Retreats &amp; Workshops</a></div>
  <div class="f-col" style="left:741px"><h4>MORE</h4><a href="#">Events</a><a href="#">Work With Me</a><a href="#">About Me</a><a href="#">Testimonials</a><a href="#">Contact</a></div>
  <a href="#" class="btn btn-line" style="left:944px;top:31px;width:173px;height:44px;font-size:11px;border-color:var(--orange);color:var(--orange)">BOOK A SESSION</a>
  <div class="abs" style="left:0;top:174px;width:1200px;text-align:center;font-size:10.5px;color:#e6eaec">© 2025 Liesbet Oonwerk. All rights reserved.</div>
</footer>
<div class="social" style="left:942px" aria-label="Photo sharing profile"></div>
<div class="social" style="left:1010px" aria-label="Social profile"></div>
<div class="social" style="left:1076px" aria-label="Email">
  <svg width="16" height="12" viewBox="0 0 16 12" fill="none" stroke="#e6eaec" stroke-width="1.2"><rect x=".6" y=".6" width="14.8" height="10.8"/><path d="M.6.6L8 6.5 15.4.6"/></svg>
</div>

</body>
</html>
```